Vo Lunec - Business Cards & Stationnery
Think Ahead, Vo Lunec
Professional
Odile Fenwar Quintanel
48 rue des Glycines Doréales
75020 Paris
France
odile@volunec.com
www.volunec.com
The business cards have to be at the european standard ie 8,5 x 5,4 cm (seems to be 3.35'' x 2.13'')
Same for the stationnery ie A4 format, 21 x 29,7 cm (seems to be 8,27'' x 11.7'')
Please use the logo, name of the company and the base line: Think Ahead, Vo Lunec

```html
<!DOCTYPE html>
<html lang="fr">
<head>
<meta charset="utf-8">
<title>Vo Lunec – Carte de visite</title>
<link rel="stylesheet" href="https://fonts.googleapis.com/css2?family=Michroma&family=Open+Sans:wght@400;600&display=swap">
<style>
  :root {
    --page-bg: #e9e7ea;
    --card-white: #ffffff;
    --brand-purple: #5e2d7c;
    --brand-purple-light: #8a5aa8;
    --brand-purple-dark: #4a1f63;
    --swoosh-grey: #6b6b6e;
    --ink-dark: #2b2b2e;
    --ink-light: #ffffff;
  }
  html, body {
    margin: 0;
    width: 1200px;
    height: 778px;
    overflow: hidden;
    background: var(--page-bg);
  }
  .business-card {
    position: absolute;
    left: 60px;
    top: 46px;
    width: 1080px;
    height: 686px;
    border-radius: 32px;
    overflow: hidden;
    background: var(--card-white);
    box-shadow: 0 2px 6px rgba(0,0,0,0.15);
  }
  .card-shapes {
    position: absolute;
    inset: 0;
  }
  .brand-block {
    position: absolute;
    left: 0;
    right: 0;
    top: 190px;
    text-align: center;
  }
  .brand-name {
    display: inline-flex;
    align-items: center;
    gap: 18px;
    font-family: "Michroma", sans-serif;
    font-size: 50px;
    color: var(--ink-dark);
    letter-spacing: 2px;
    line-height: 1;
  }
  .brand-square {
    width: 34px;
    height: 34px;
    background: var(--brand-purple);
  }
  .brand-tagline {
    margin-top: 14px;
    font-family: "Michroma", sans-serif;
    font-size: 15px;
    letter-spacing: 3px;
    color: var(--ink-dark);
    text-transform: uppercase;
  }
  .holder-name {
    position: absolute;
    left: 64px;
    top: 503px;
    font-family: "Open Sans", sans-serif;
    font-weight: 600;
    font-size: 27px;
    color: var(--ink-light);
  }
  .divider {
    position: absolute;
    left: 562px;
    top: 405px;
    width: 2px;
    height: 250px;
    background: rgba(255,255,255,0.75);
  }
  .contact-list {
    position: absolute;
    left: 584px;
    top: 410px;
    margin: 0;
    padding: 0;
    list-style: none;
    font-family: "Open Sans", sans-serif;
    font-size: 22px;
    line-height: 34px;
    color: var(--ink-light);
  }
  .contact-list .gap { margin-top: 6px; }
  .contact-list .icon-row {
    display: flex;
    align-items: center;
    gap: 12px;
  }
  .contact-icon {
    width: 18px;
    height: 18px;
    flex: none;
  }
</style>
</head>
<body>
  <div class="business-card">
    <svg class="card-shapes" width="1080" height="686" viewBox="0 0 1080 686">
      <defs>
        <radialGradient id="purpleGlow" cx="0.45" cy="0.55" r="0.7">
          <stop offset="0" stop-color="var(--brand-purple-light)"/>
          <stop offset="0.6" stop-color="var(--brand-purple)"/>
          <stop offset="1" stop-color="var(--brand-purple-dark)"/>
        </radialGradient>
      </defs>
      <path class="swoosh" d="M0,338 C320,410 640,372 1080,262 L1080,312 C640,400 320,420 0,352 Z" fill="var(--swoosh-grey)"/>
      <path class="purple-band" d="M0,352 C320,420 640,400 1080,312 L1080,686 L0,686 Z" fill="url(#purpleGlow)"/>
    </svg>

    <div class="brand-block">
      <div class="brand-name"><span class="brand-square"></span>VO LUNEC</div>
      <div class="brand-tagline">Think Ahead, Vo Lunec</div>
    </div>

    <div class="holder-name">Odile Fenwar Quintanel</div>
    <div class="divider"></div>

    <ul class="contact-list">
      <li>48 rue des Glycines Doréales</li>
      <li>75020 Paris</li>
      <li>France</li>
      <li class="icon-row gap">
        <svg class="contact-icon" viewBox="0 0 18 18"><rect x="5" y="1" width="8" height="16" rx="1.5" fill="#fff"/><rect x="6.5" y="3" width="5" height="9" fill="var(--brand-purple)"/></svg>
        +33 (0)6 47 18 52 30
      </li>
      <li class="icon-row">
        <svg class="contact-icon" viewBox="0 0 18 18"><rect x="1" y="4" width="16" height="11" fill="#fff"/><path d="M1.5,4.5 L9,10.5 L16.5,4.5" fill="none" stroke="var(--brand-purple)" stroke-width="1.4"/></svg>
        odile@volunec.com
      </li>
      <li class="icon-row">
        <svg class="contact-icon" viewBox="0 0 18 18"><circle cx="9" cy="9" r="8" fill="#fff"/><ellipse cx="9" cy="9" rx="3.5" ry="8" fill="none" stroke="var(--brand-purple)" stroke-width="1.2"/><path d="M1,9 H17" stroke="var(--brand-purple)" stroke-width="1.2"/></svg>
        www.volunec.com
      </li>
    </ul>
  </div>
</body>
</html>
```